R&t Subterra

We specialize in CIPP pipe lining but do other underground utilities trenchless as well.

Target Market(s)

Trenchless sewer replacement

Contact Information for Business Card

Gavin Holtby 715-482-6130 Pine Hollow, wi

```html
<!DOCTYPE html>
<html lang="en">
<head>
<meta charset="utf-8">
<title>R&amp;t Subterra – Business Card</title>
<link rel="stylesheet" href="https://fonts.googleapis.com/css2?family=Montserrat:wght@400;500;700&family=Open+Sans:wght@400&display=swap">
<style>
  :root {
    --stage: #e9eaec;
    --card: #ffffff;
    --brand-blue: #3590cf;
    --deep-blue: #0a6fc2;
    --band-grey: #b3b3b3;
    --ink: #1c1c1c;
    --rule: #222222;
  }
  * { box-sizing: border-box; margin: 0; padding: 0; }
  html, body { width: 1200px; height: 895px; overflow: hidden; }
  body {
    background: var(--stage);
    font-family: "Montserrat", sans-serif;
    display: flex;
    flex-direction: column;
    align-items: center;
    justify-content: center;
    gap: 30px;
  }
  .card {
    position: relative;
    width: 700px;
    height: 400px;
    background: var(--card);
    box-shadow: 0 6px 18px rgba(0,0,0,.12);
    overflow: hidden;
  }
  .brand {
    display: flex;
    align-items: center;
    gap: 18px;
    color: var(--brand-blue);
    font-weight: 700;
    white-space: nowrap;
  }
  .brand-dot {
    flex: none;
    border-radius: 50%;
    background: var(--brand-blue);
  }
  .card-front .brand {
    position: absolute;
    inset: 0;
    justify-content: center;
    font-size: 58px;
  }
  .card-front .brand-dot { width: 60px; height: 60px; }
  .card-back .brand {
    position: absolute;
    top: 58px;
    right: 48px;
    font-size: 32px;
    gap: 12px;
  }
  .card-back .brand-dot { width: 34px; height: 34px; }
  .person { position: absolute; left: 44px; top: 196px; }
  .person-name {
    color: var(--brand-blue);
    font-weight: 700;
    font-size: 30px;
    letter-spacing: .3px;
  }
  .person-title {
    color: var(--ink);
    font-weight: 400;
    font-size: 19px;
    margin-top: 4px;
  }
  .divider {
    position: absolute;
    left: 44px;
    right: 40px;
    top: 276px;
    height: 1.5px;
    background: var(--rule);
  }
  .contact-list {
    position: absolute;
    top: 292px;
    list-style: none;
    font-family: "Open Sans", sans-serif;
    font-size: 17px;
    color: var(--ink);
  }
  .contact-list li {
    display: flex;
    align-items: center;
    gap: 12px;
    height: 28px;
    white-space: nowrap;
  }
  .contact-list svg { width: 18px; height: 18px; fill: var(--deep-blue); flex: none; }
  .contact-left { left: 60px; }
  .contact-right { left: 440px; }
  .bottom-band { position: absolute; left: 0; bottom: 0; width: 700px; height: 60px; }
</style>
</head>
<body>
  <section class="card card-front">
    <div class="brand"><span class="brand-dot"></span>R&amp;t Subterra</div>
  </section>

  <section class="card card-back">
    <div class="brand"><span class="brand-dot"></span>R&amp;t Subterra</div>

    <div class="person">
      <h1 class="person-name">Gavin Holtby</h1>
      <p class="person-title">Managing Director</p>
    </div>

    <div class="divider"></div>

    <ul class="contact-list contact-left">
      <li>
        <svg viewBox="0 0 24 24" aria-hidden="true"><path d="M6.6 10.8a15.1 15.1 0 0 0 6.6 6.6l2.2-2.2a1 1 0 0 1 1-.25 11.4 11.4 0 0 0 3.6.57 1 1 0 0 1 1 1V20a1 1 0 0 1-1 1A17 17 0 0 1 3 4a1 1 0 0 1 1-1h3.5a1 1 0 0 1 1 1c0 1.25.2 2.45.57 3.6a1 1 0 0 1-.25 1z"/></svg>
        715-482-6130
      </li>
      <li>
        <svg viewBox="0 0 24 24" aria-hidden="true"><path d="M2 5h20v14H2z"/><path d="M3 6l9 7 9-7" fill="none" stroke="#fff" stroke-width="1.6"/></svg>
        hello@rtsubterra.com
      </li>
    </ul>

    <ul class="contact-list contact-right">
      <li>
        <svg viewBox="0 0 24 24" aria-hidden="true"><circle cx="12" cy="12" r="10"/><path d="M2.5 12h19M12 2.5c3 3 3 16 0 19M12 2.5c-3 3-3 16 0 19" fill="none" stroke="#fff" stroke-width="1.4"/></svg>
        www.rtsubterra.com
      </li>
      <li>
        <svg viewBox="0 0 24 24" aria-hidden="true"><path d="M12 2a7 7 0 0 0-7 7c0 5 7 13 7 13s7-8 7-13a7 7 0 0 0-7-7zm0 9.5A2.5 2.5 0 1 1 12 6.5a2.5 2.5 0 0 1 0 5z"/></svg>
        Pine Hollow, wi
      </li>
    </ul>

    <svg class="bottom-band" viewBox="0 0 700 60" preserveAspectRatio="none" aria-hidden="true">
      <polygon points="500,36 700,36 700,60 476,60" fill="var(--band-grey)"/>
      <polygon points="0,46 480,46 466,60 0,60" fill="var(--deep-blue)"/>
    </svg>
  </section>
</body>
</html>
```